Steady Valve Systems

I need a business card with the attached logo.
The second page I have attached is what we are looking for. We want doubles sided. We would like the blues fading and the logo on the back.

Industry/Entity Type

Business

```html
<!DOCTYPE html>
<html lang="en">
<head>
<meta charset="utf-8">
<title>Steady Valve Systems – Business Card</title>
<link href="https://fonts.googleapis.com/css2?family=Michroma&display=swap" rel="stylesheet">
<style>
  :root {
    --page-bg: #1a1c20;
    --card-white: #f3f4f6;
    --card-grey: #dfe2e6;
    --brand-blue: #2f5f9e;
    --band-blue: #3a6cb0;
    --sky-light: #d9f2fb;
    --sky-mid: #3aa7dc;
    --sky-deep: #1e5fb0;
    --navy: #13316f;
    --text-white: #ffffff;
    --title-blue: #1f4f9a;
  }
  * { margin: 0; padding: 0; box-sizing: border-box; }
  html, body {
    width: 1200px; height: 871px; overflow: hidden;
    background: var(--page-bg);
    font-family: "Michroma", sans-serif;
  }
  .canvas {
    width: 1200px; height: 871px;
    display: flex; flex-direction: column; align-items: center; justify-content: center;
    gap: 36px;
  }
  .card {
    position: relative;
    width: 665px; height: 380px;
    overflow: hidden;
  }

  /* Back side */
  .card-back {
    background: linear-gradient(160deg, var(--card-white) 0%, var(--card-grey) 100%);
  }
  .card-back .brand {
    position: absolute; left: 0; right: 0; top: 110px;
    text-align: center;
  }
  .brand-name {
    color: var(--brand-blue);
    font-size: 30px; letter-spacing: 2px;
  }
  .brand-sub {
    color: var(--brand-blue);
    font-size: 13px; letter-spacing: 6px; margin-top: 8px;
  }
  .website {
    margin-top: 22px;
    color: var(--brand-blue);
    font-size: 15px; letter-spacing: 4px;
  }
  .accent-band {
    position: absolute; left: 0; right: 0; top: 250px; height: 8px;
    background: var(--band-blue);
  }
  .address-band {
    position: absolute; left: 0; right: 0; bottom: 40px; height: 34px;
    background: var(--band-blue);
    display: flex; align-items: center; justify-content: center; gap: 10px;
    color: var(--text-white); font-size: 12px; letter-spacing: 3px;
  }

  /* Front side */
  .card-front {
    background:
      radial-gradient(ellipse 70% 60% at 25% 10%, var(--sky-light) 0%, rgba(217,242,251,0) 70%),
      linear-gradient(150deg, var(--sky-mid) 0%, var(--sky-deep) 60%, var(--navy) 100%);
  }
  .card-front .brand {
    position: absolute; left: 150px; top: 40px;
    text-align: center;
  }
  .card-front .brand-name { color: var(--title-blue); font-size: 28px; }
  .card-front .brand-sub { color: var(--title-blue); font-size: 12px; }
  .contact {
    position: absolute; left: 110px; top: 220px;
    color: var(--text-white);
  }
  .person-name { font-size: 34px; letter-spacing: 2px; }
  .job-title {
    color: var(--title-blue); font-size: 13px; letter-spacing: 5px; margin-top: 4px;
  }
  .phone {
    display: flex; align-items: center; gap: 12px;
    font-size: 18px; letter-spacing: 6px; margin-top: 12px;
  }
</style>
</head>
<body>
<main class="canvas">
  <section class="card card-back" aria-label="Card back">
    <div class="brand">
      <div class="brand-name">STEADY VALVE</div>
      <div class="brand-sub">· SYSTEMS ·</div>
      <div class="website">YOUR WEBSITE</div>
    </div>
    <div class="accent-band"></div>
    <div class="address-band">
      <svg width="12" height="16" viewBox="0 0 12 16" aria-hidden="true">
        <path d="M6 0a6 6 0 0 0-6 6c0 4.5 6 10 6 10s6-5.5 6-10a6 6 0 0 0-6-6z" fill="#ffffff"/>
        <circle cx="6" cy="6" r="2.2" fill="#3a6cb0"/>
      </svg>
      <span>123 MAIN STREET, CITY, USA-21212</span>
    </div>
  </section>

  <section class="card card-front" aria-label="Card front">
    <div class="brand">
      <div class="brand-name">STEADY VALVE</div>
      <div class="brand-sub">· SYSTEMS ·</div>
    </div>
    <div class="contact">
      <div class="person-name">Your Name</div>
      <div class="job-title">JOB TITLE</div>
      <div class="phone">
        <svg width="22" height="18" viewBox="0 0 22 18" aria-hidden="true">
          <path d="M1 5c0-3 20-3 20 0v2h-5V5H6v2H1z" fill="#ffffff"/>
          <path d="M5 8h12l3 9H2z" fill="#ffffff"/>
          <circle cx="11" cy="12.5" r="2.4" fill="#2a7fc6"/>
        </svg>
        <span>000-000-0000</span>
      </div>
    </div>
  </section>
</main>
</body>
</html>
```